Podcast Marketing Template for LinkedIn

I would like to have graphics to post notices of new podcast episodes on LinkedIn as release new episodes.
The graphics need to be in a template form that can be easily updated by my VA.
Each episode will have a new title and guest.
Two examples of a ROUGH DRAFT of an episode example are attached.
(I do not like these because I think they reflect the standards I have for my brand.)
The posts should be bright and clean and clearly reflect QUALITY of the podcast in the quality of the design. Audience and interviewees are CEOs.
Please refer to my website and podcast art to see brand direction.
www.lennartoswaldadvisory.com
Each

```html
<!DOCTYPE html>
<html lang="en">
<head>
<meta charset="utf-8">
<title>Rising Fortune Podcast – Episode Graphics</title>
<link rel="stylesheet" href="https://fonts.googleapis.com/css2?family=Oswald:wght@300;600&family=Poppins:wght@400;500;800&family=Kaushan+Script&display=swap">
<style>
  :root{
    --page:#ffffff;
    --ink:#1a1a1a;
    --navy-deep:#0d2c57;
    --navy:#16457f;
    --navy-light:#2a64a3;
    --accent:#3ba4e6;
    --band:#2b77bd;
    --white:#ffffff;
    --photo-a:#c9d6e6;
    --photo-b:#5c7fa8;
  }
  html,body{margin:0;padding:0;}
  body{
    width:800px;height:1200px;overflow:hidden;
    background:var(--page);
    position:relative;
    font-family:"Poppins",sans-serif;
  }
  .size-label{
    position:absolute;left:0;width:800px;margin:0;
    text-align:center;font-weight:400;font-size:28px;color:var(--ink);
    letter-spacing:.5px;
  }
  .size-label--square{top:86px;}
  .size-label--wide{top:633px;}
  .episode-card{
    position:absolute;display:block;
    filter:drop-shadow(0 12px 18px rgba(0,0,0,.28));
  }
  .episode-card--square{left:184px;top:145px;width:432px;height:432px;}
  .episode-card--wide{left:53px;top:687px;width:694px;height:391px;}
  .show-name{font-family:"Poppins",sans-serif;font-weight:500;fill:var(--white);}
  .title{font-family:"Oswald",sans-serif;fill:var(--white);}
  .title-bold{font-weight:600;}
  .title-light{font-weight:300;}
  .title-accent{font-weight:600;fill:var(--accent);}
  .with{font-family:"Kaushan Script",cursive;fill:var(--white);}
  .person-name{font-family:"Poppins",sans-serif;font-weight:800;fill:var(--white);}
  .person-role{font-family:"Poppins",sans-serif;font-weight:400;fill:var(--white);}
</style>
</head>
<body>

<p class="size-label size-label--square">1080x1080px</p>

<svg class="episode-card episode-card--square" viewBox="0 0 432 432" xmlns="http://www.w3.org/2000/svg">
  <defs>
    <linearGradient id="sq-bg" x1="0" y1="0" x2="1" y2="1">
      <stop offset="0" stop-color="#123b70"/>
      <stop offset=".55" stop-color="#16457f"/>
      <stop offset="1" stop-color="#0e2f5c"/>
    </linearGradient>
    <radialGradient id="photo-fill" cx=".5" cy=".4" r=".7">
      <stop offset="0" stop-color="#c9d6e6"/>
      <stop offset="1" stop-color="#5c7fa8"/>
    </radialGradient>
  </defs>
  <rect class="card-bg" width="432" height="432" fill="url(#sq-bg)" role="img" aria-label="Blue city skyline with network lines"/>

  <g class="show-brand">
    <rect x="124" y="27" width="60" height="60" fill="#dfe6ee"/>
    <text class="show-name" font-size="20"><tspan x="194" y="43">Rising</tspan><tspan x="194" y="65">Fortune</tspan><tspan x="194" y="86">Podcast</tspan></text>
  </g>

  <g class="episode-title">
    <text class="title" x="60" y="150" font-size="54" textLength="312" lengthAdjust="spacingAndGlyphs"><tspan class="title-bold">TECHNOLOGY </tspan><tspan class="title-light">AND</tspan></text>
    <text class="title" x="60" y="204" font-size="54" textLength="311" lengthAdjust="spacingAndGlyphs"><tspan class="title-bold">PHILANTHROPY </tspan><tspan class="title-light">IN</tspan></text>
    <text class="title title-accent" x="60" y="278" font-size="83" textLength="309" lengthAdjust="spacingAndGlyphs">EDUCATION</text>
  </g>

  <g class="guest">
    <polygon points="124,313 262,313 269,333 124,333" fill="var(--band)"/>
    <circle cx="80" cy="357" r="53" fill="var(--band)"/>
    <circle cx="80" cy="357" r="48" fill="url(#photo-fill)" role="img" aria-label="Portrait photo of guest Tomas Veldhuis"/>
    <text class="with" x="141" y="310" font-size="12">with</text>
    <text class="person-name" x="141" y="328" font-size="14">TOMAS VELDHUIS</text>
    <text class="person-role" x="141" y="349" font-size="10.5">CEO of Novaleaf</text>
  </g>

  <g class="host">
    <polygon points="152,359 305,359 305,378 145,378" fill="var(--band)"/>
    <text class="person-name" x="293" y="374" font-size="14" text-anchor="end">LENNART OSWALD</text>
    <text class="person-role" x="293" y="392" font-size="10.5" text-anchor="end">Host</text>
    <circle cx="350" cy="357" r="53" fill="var(--band)"/>
    <circle cx="350" cy="357" r="48" fill="url(#photo-fill)" role="img" aria-label="Portrait photo of host Lennart Oswald"/>
  </g>
</svg>

<p class="size-label size-label--wide">1920x1080px</p>

<svg class="episode-card episode-card--wide" viewBox="0 0 694 391" xmlns="http://www.w3.org/2000/svg">
  <defs>
    <linearGradient id="wd-bg" x1="0" y1="0" x2="1" y2="1">
      <stop offset="0" stop-color="#123b70"/>
      <stop offset=".6" stop-color="#16457f"/>
      <stop offset="1" stop-color="#2a5f98"/>
    </linearGradient>
    <radialGradient id="photo-fill-w" cx=".5" cy=".4" r=".7">
      <stop offset="0" stop-color="#c9d6e6"/>
      <stop offset="1" stop-color="#5c7fa8"/>
    </radialGradient>
  </defs>
  <rect class="card-bg" width="694" height="391" fill="url(#wd-bg)" role="img" aria-label="Blue city skyline with network lines"/>
  <rect class="accent-band" x="448" y="0" width="62" height="391" fill="var(--band)"/>

  <g class="show-brand">
    <rect x="33" y="45" width="67" height="67" fill="#dfe6ee"/>
    <text class="show-name" font-size="25"><tspan x="111" y="62">Rising</tspan><tspan x="111" y="87">Fortune</tspan><tspan x="111" y="111">Podcast</tspan></text>
  </g>

  <g class="episode-title">
    <text class="title" x="33" y="183" font-size="60" textLength="366" lengthAdjust="spacingAndGlyphs"><tspan class="title-bold">TECHNOLOGY </tspan><tspan class="title-light">AND</tspan></text>
    <text class="title" x="33" y="245" font-size="60" textLength="363" lengthAdjust="spacingAndGlyphs"><tspan class="title-bold">PHILANTHROPY </tspan><tspan class="title-light">IN</tspan></text>
    <text class="title title-accent" x="33" y="333" font-size="99" textLength="360" lengthAdjust="spacingAndGlyphs">EDUCATION</text>
  </g>

  <g class="guest">
    <circle cx="480" cy="124" r="65" fill="var(--accent)"/>
    <circle cx="480" cy="124" r="59" fill="url(#photo-fill-w)" role="img" aria-label="Portrait photo of guest Tomas Veldhuis"/>
    <text class="with" x="556" y="92" font-size="15">with</text>
    <text class="person-name" font-size="27"><tspan x="555" y="118">TOMAS</tspan><tspan x="555" y="144">VELDHUIS</tspan></text>
    <text class="person-role" x="555" y="165" font-size="15.5">CEO of Novaleaf</text>
  </g>

  <g class="host">
    <circle cx="480" cy="279" r="65" fill="var(--accent)"/>
    <circle cx="480" cy="279" r="59" fill="url(#photo-fill-w)" role="img" aria-label="Portrait photo of host Lennart Oswald"/>
    <text class="person-name" font-size="27"><tspan x="555" y="274">LENNART</tspan><tspan x="555" y="301">OSWALD</tspan></text>
    <text class="person-role" x="556" y="322" font-size="15.5">Host</text>
  </g>
</svg>

</body>
</html>
```